Luminously Grounded Vitality

We want to design a business card that is modern and appealing for an innovative psychedelic telemedicine company that provides at-home ketamine-assisted therapy along with wellness, longevity, and anti-aging medicines. We want to use our deep purple and white plus other colors you can find on our website. We don't have any strict brand guidelines yet so feel free to get creative. We want a very professional, but technology first modern design that will instill trust, peace, calm, but also be attractive to investors in the healthcare and SaaS space.

```html
<!DOCTYPE html>
<html lang="en">
<head>
<meta charset="utf-8">
<title>Luminously Grounded Vitality — Business Card</title>
<link rel="stylesheet" href="https://fonts.googleapis.com/css2?family=Open+Sans:wght@300;400;600&display=swap">
<style>
  :root {
    --canvas: #ece9ee;
    --purple-deep: #54308f;
    --purple-mid: #6c3598;
    --magenta: #8f3a98;
    --lilac: #b07cc0;
    --paper: #fdf4f2;
    --ink: #4a2478;
    --white: #ffffff;
  }
  * { margin: 0; padding: 0; box-sizing: border-box; }
  html, body { width: 1200px; height: 892px; overflow: hidden; }
  body {
    background: var(--canvas);
    font-family: "Open Sans", Arial, sans-serif;
    display: flex;
    flex-direction: column;
    align-items: center;
    justify-content: center;
    gap: 56px;
  }
  .card {
    position: relative;
    width: 560px;
    height: 320px;
    overflow: hidden;
    border-radius: 2px;
    box-shadow: 0 10px 28px rgba(60, 30, 90, 0.18);
  }

  /* Front: purple field with a plain paper column on the right */
  .card--front { background: linear-gradient(170deg, var(--purple-mid) 0%, var(--purple-deep) 100%); }
  .front__column {
    position: absolute;
    top: 0; right: 0; bottom: 0;
    width: 120px;
    background: var(--paper);
    border-left: 8px solid var(--magenta);
  }
  .front__rule {
    position: absolute;
    top: 0; bottom: 0;
    right: 136px;
    width: 2px;
    background: var(--lilac);
    opacity: 0.5;
  }
  .wordmark {
    position: absolute;
    left: 40px;
    width: 360px;
    top: 114px;
    display: flex;
    flex-direction: column;
    align-items: center;
    gap: 10px;
  }
  .wordmark__dot {
    width: 22px; height: 22px; border-radius: 50%;
    background: var(--lilac);
  }
  .wordmark__name {
    font-weight: 300;
    font-size: 34px;
    letter-spacing: 1px;
    color: var(--white);
  }

  /* Back: paper with a straight purple footer band */
  .card--back { background: var(--paper); }
  .back__band {
    position: absolute;
    left: 0; right: 0; bottom: 0;
    height: 64px;
    background: linear-gradient(90deg, var(--purple-mid) 0%, var(--purple-deep) 100%);
    border-top: 6px solid var(--magenta);
  }
  .identity {
    position: absolute;
    top: 24px;
    left: 0; right: 0;
    text-align: center;
    color: var(--ink);
  }
  .identity__dot {
    width: 16px; height: 16px; border-radius: 50%;
    background: var(--lilac);
    margin: 0 auto 6px;
  }
  .identity__name { font-weight: 600; font-size: 15px; line-height: 1.25; }
  .contact {
    position: absolute;
    top: 98px;
    left: 64px;
    list-style: none;
    color: var(--ink);
    font-size: 12.5px;
    font-weight: 600;
    line-height: 1.35;
  }
  .contact__item { display: flex; align-items: flex-start; gap: 14px; margin-bottom: 9px; }
  .contact__icon { width: 16px; height: 16px; flex: none; fill: var(--ink); margin-top: 1px; }
</style>
</head>
<body>

  <section class="card card--front" aria-label="Card front">
    <div class="front__rule"></div>
    <div class="front__column"></div>
    <div class="wordmark">
      <span class="wordmark__dot"></span>
      <span class="wordmark__name">Luminously</span>
    </div>
  </section>

  <section class="card card--back" aria-label="Card back">
    <div class="back__band"></div>

    <header class="identity">
      <div class="identity__dot"></div>
      <p class="identity__name">Luminously<br>Grounded Vitality, PBC</p>
    </header>

    <ul class="contact">
      <li class="contact__item">
        <svg class="contact__icon" viewBox="0 0 24 24" aria-label="Phone"><path d="M6.6 10.8a15 15 0 0 0 6.6 6.6l2.2-2.2a1 1 0 0 1 1-.25 11.4 11.4 0 0 0 3.6.57 1 1 0 0 1 1 1V20a1 1 0 0 1-1 1A17 17 0 0 1 3 4a1 1 0 0 1 1-1h3.5a1 1 0 0 1 1 1c0 1.25.2 2.45.57 3.57a1 1 0 0 1-.25 1z"/></svg>
        <span>833-555-0142</span>
      </li>
      <li class="contact__item">
        <svg class="contact__icon" viewBox="0 0 24 24" aria-label="Address"><path d="M12 2a7 7 0 0 0-7 7c0 5.2 7 13 7 13s7-7.8 7-13a7 7 0 0 0-7-7zm0 9.5A2.5 2.5 0 1 1 12 6.5a2.5 2.5 0 0 1 0 5z"/></svg>
        <span>482 Alder Street, Suite 900<br>Boulder, Colorado 80302</span>
      </li>
      <li class="contact__item">
        <svg class="contact__icon" viewBox="0 0 24 24" aria-label="Email"><path d="M4 3h16a2 2 0 0 1 2 2v10a2 2 0 0 1-2 2H9l-5 4v-4a2 2 0 0 1-2-2V5a2 2 0 0 1 2-2zm3 5v1.5h10V8zm0 3.5V13h7v-1.5z"/></svg>
        <span>hello@luminouslyvitality.com</span>
      </li>
    </ul>
  </section>

</body>
</html>
```